Full Page Magazine Ad for Law Firm

Full Page Magazine Ad

The project is to design a full page ad to be place in Cannabis Harvest magazine in the November 2017 edition.

Purpose of the ad is to promote Brightwater Law Group and not Martin Sloane from ms LAW ad.

About 20% of Brightwater Law Group’s current practice is marijuana related and it is looking grow that by illustrating in the ad that ms LAW is joining the firm.

Brightwater Law Group offers services in
• Tax Law
• Securities & Finance
• Business & Corporations
• Business Structuring
• Investments Funds & Management
• Rest Estate
• Outside General Counsel

ms LAW has offered services in:

• Marijuana regulation and compliance
• Buying and selling marijuana businesses
• Business & Corporations

Color palate should match Brightwater Law Group logo (blue) color with gray, black, white.

DO NOT want marijuana leaf images.
DO NOT include picture of Martin Sloane from ms LAW ad.

Documents provided:
Brightwater Law Group logo
Past ms LAW ad in magazine
Examples of competitor ads in same publication
Magazine spec sheet

Target Market(s)

The target of the ad is owners of larger marijuana retail stores and marijuana production/processing operations that need legal services.

Industry/Entity Type

Law Firm

Font styles to use
Other font styles liked:
• Should fit with BWLG logo.

Colors
3276b5

Requirements
Must have
• Brightwater Law Group is the Primary focus
• Use Brightwater Law Group address / contact information
• Ad must make clear that Brightwater Law Group is a Law Firm offering legal services to businesses.
Should not have
• DO NOT want marijuana leaf images.
• DO NOT include picture of Martin Sloane from ms LAW ad

```html
<!DOCTYPE html>
<html lang="en">
<head>
<meta charset="utf-8">
<title>Brightwater Law Group – Magazine Ad</title>
<link href="https://fonts.googleapis.com/css2?family=Marcellus&family=Open+Sans:wght@300;400;600&display=swap" rel="stylesheet">
<style>
  :root {
    --brand-blue: #3276b5;
    --title-blue: #3a73ad;
    --ink: #3c3c3c;
    --ink-dark: #1e1e1e;
    --panel-grey: #e8e9e9;
    --paper: #ffffff;
    --backdrop: #d6d6d6;
    --photo-top: #e9e4dc;
    --photo-bottom: #8a7560;
  }
  * { box-sizing: border-box; margin: 0; padding: 0; }
  html, body { width: 960px; height: 1200px; overflow: hidden; background: var(--backdrop); }
  .ad {
    position: absolute; left: 30px; top: 0;
    width: 900px; height: 1200px;
    background: var(--paper);
    font-family: "Open Sans", Arial, sans-serif;
    color: var(--ink);
  }
  .hero-photo {
    position: absolute; left: 18px; top: 19px; width: 864px; height: 589px;
    background: linear-gradient(180deg, var(--photo-top) 0%, #cdbfae 45%, var(--photo-bottom) 100%);
  }
  .firm-name {
    position: absolute; left: 78px; top: 628px;
    font-family: "Marcellus", Georgia, serif;
    font-size: 47px; color: var(--title-blue); white-space: nowrap; letter-spacing: 0.5px;
  }
  .firm-name .suffix { font-size: 29px; margin-left: 6px; }
  .merge-line {
    position: absolute; left: 78px; top: 700px; display: flex; align-items: flex-end; white-space: nowrap;
  }
  .merge-line .lead { font-weight: 300; font-size: 45px; color: var(--ink); letter-spacing: 0.5px; }
  .merge-line .partner-name {
    margin-left: 22px; font-weight: 600; font-size: 72px; line-height: 1; color: var(--ink-dark);
    position: relative; top: -4px;
  }
  .services {
    position: absolute; left: 18px; top: 781px; width: 864px; height: 303px;
    background: var(--panel-grey);
  }
  .service-col { position: absolute; top: 30px; }
  .service-col.primary { left: 61px; width: 341px; }
  .service-col.partner { left: 473px; width: 293px; }
  .service-col h2 {
    font-size: 24px; font-weight: 600; color: var(--brand-blue); line-height: 28px;
    padding-bottom: 4px; border-bottom: 2px solid var(--brand-blue); text-transform: uppercase;
  }
  .service-col ul { list-style: none; margin-top: 16px; font-size: 18.5px; color: #4a4a4a; }
  .service-col li { line-height: 27.5px; white-space: nowrap; }
  .service-col li.spaced { margin-top: 4px; }
  .service-col li::before { content: "• "; font-size: 14px; vertical-align: 2px; }
  .service-col li span + span { margin-left: 12px; }
  .contact-bar {
    position: absolute; left: 0; top: 1083px; width: 900px; height: 117px;
    background: var(--brand-blue); color: #fff; font-size: 17.5px;
  }
  .contact-item {
    position: absolute; top: 0; height: 117px; text-align: center;
    display: flex; flex-direction: column; align-items: center; justify-content: center; gap: 16px;
  }
  .contact-item svg { width: 18px; height: 18px; fill: #fff; }
  .contact-item.address { left: 0; width: 352px; padding-left: 40px; }
  .contact-item.phone { left: 352px; width: 142px; }
  .contact-item.web { left: 494px; width: 184px; }
  .contact-item.mail { left: 678px; width: 222px; }
  .divider { position: absolute; top: 25px; width: 2px; height: 71px; background: #fff; }
</style>
</head>
<body>
<main class="ad">
  <div class="hero-photo" role="img" aria-label="Photo of a business team meeting with a client around a wooden office table"></div>

  <h1 class="firm-name">BRIGHTWATER LAW GROUP<span class="suffix">PLLC</span></h1>
  <p class="merge-line"><span class="lead">HAS MERGED WITH</span><span class="partner-name">ms LAW</span></p>

  <section class="services">
    <div class="service-col primary">
      <h2>Brightwater Law Group offers services in</h2>
      <ul>
        <li><span>Tax Law</span> <span>• Rest Estate</span></li>
        <li>Securities &amp; Finance</li>
        <li>Business &amp; Corporations</li>
        <li class="spaced">Business Structuring</li>
        <li class="spaced">Investments Funds &amp; Management</li>
        <li class="spaced">Outside General Counsel</li>
      </ul>
    </div>
    <div class="service-col partner">
      <h2>ms LAW has offered services in:</h2>
      <ul>
        <li>Marijuana regulation and compliance</li>
        <li>Buying and selling marijuana businesses</li>
        <li>Business &amp; Corporations</li>
      </ul>
    </div>
  </section>

  <footer class="contact-bar">
    <div class="contact-item address">
      <svg viewBox="0 0 24 24" aria-hidden="true"><path d="M12 2a7 7 0 0 0-7 7c0 5 7 13 7 13s7-8 7-13a7 7 0 0 0-7-7zm0 9.5A2.5 2.5 0 1 1 12 6.5a2.5 2.5 0 0 1 0 5z"/></svg>
      <span>123 Harbor St. Lakeview, FL 32900</span>
    </div>
    <div class="divider" style="left:352px"></div>
    <div class="contact-item phone">
      <svg viewBox="0 0 24 24" aria-hidden="true"><path d="M3 9c0-3 4-5 9-5s9 2 9 5v2h-5V9H8v2H3zM6 12h12l2 8H4z"/></svg>
      <span>123-456-789</span>
    </div>
    <div class="divider" style="left:494px"></div>
    <div class="contact-item web">
      <svg viewBox="0 0 24 24" aria-hidden="true"><path d="M12 2a10 10 0 1 0 0 20 10 10 0 0 0 0-20zm7.9 9h-3.4a15 15 0 0 0-1.3-6 8 8 0 0 1 4.7 6zM12 4c1 1.4 2.2 3.9 2.5 7h-5C9.8 7.9 11 5.4 12 4zM8.8 5a15 15 0 0 0-1.3 6H4.1a8 8 0 0 1 4.7-6zM4.1 13h3.4a15 15 0 0 0 1.3 6 8 8 0 0 1-4.7-6zM12 20c-1-1.4-2.2-3.9-2.5-7h5c-.3 3.1-1.5 5.6-2.5 7zm3.2-1a15 15 0 0 0 1.3-6h3.4a8 8 0 0 1-4.7 6z"/></svg>
      <span>www.website.com</span>
    </div>
    <div class="divider" style="left:678px"></div>
    <div class="contact-item mail">
      <svg viewBox="0 0 24 24" aria-hidden="true"><path d="M2 5h20v2l-10 6L2 7zm0 4.3 10 6 10-6V19H2z"/></svg>
      <span>info@website.com</span>
    </div>
  </footer>
</main>
</body>
</html>
```